Airport Advertising Brochure

I need a flyer put together asap! Previous example included. Would like something clean and updated. New logo and updated company name. I would like this designed in Pages or Illustrator so I can update content when needed. Website: pagelantern.com

Target Market(s)

Authors. This page has some good content about what we do: https://www.pagelantern.com/terminalpromos/

Industry/Entity Type

Airport

Font styles to use
Serif
Sans Serif

Requirements
Must have
• Clean, modern design.

```html
<!DOCTYPE html>
<html lang="en">
<head>
<meta charset="utf-8">
<title>Page Lantern — Terminal Promos</title>
<link rel="stylesheet" href="https://fonts.googleapis.com/css2?family=Poppins:wght@300;400;700&display=swap">
<style>
  :root {
    --plum: #3c1740;
    --paper: #ffffff;
    --ink: #231f20;
    --gold: #ffdd00;
    --frame: #58585a;
    --photo-a: #a0602e;
    --photo-b: #5a3a22;
    --photo-c: #8a7a5a;
    --photo-d: #b0413a;
  }
  * { box-sizing: border-box; margin: 0; padding: 0; }
  html, body { width: 1200px; height: 1000px; overflow: hidden; background: var(--paper); }
  body { position: relative; font-family: "Poppins", sans-serif; }

  .slide {
    position: absolute;
    border: 2px solid var(--frame);
    background: var(--plum);
    overflow: hidden;
  }
  .slide-shapes { position: absolute; left: 0; top: 0; }

  /* Cover slide */
  .slide--cover { left: 49px; top: 85px; width: 584px; height: 397px; z-index: 2; }
  .brand {
    position: absolute; left: 35px; top: 52px; width: 120px;
    display: flex; flex-direction: column; align-items: center; gap: 42px;
  }
  .brand-square { width: 16px; height: 16px; background: var(--gold); }
  .brand-name { font-size: 17px; font-weight: 400; color: var(--ink); letter-spacing: -0.2px; line-height: 20px; white-space: nowrap; }

  .reach-list {
    position: absolute; left: 290px; top: 151px; width: 300px;
    list-style: none; color: var(--paper);
    font-size: 11.5px; font-weight: 300; line-height: 15.5px;
  }
  .reach-list li { position: relative; padding-left: 13px; margin-bottom: 10px; }
  .reach-list li:first-child { margin-bottom: 2px; }
  .reach-list li::before {
    content: ""; position: absolute; left: 1px; top: 4px;
    width: 6px; height: 6px; background: var(--gold); transform: rotate(45deg);
  }

  /* Window display slide */
  .slide--window { left: 469px; top: 450px; width: 670px; height: 472px; z-index: 1; }
  .slide-title {
    position: absolute; left: 14px; top: 62px;
    font-size: 21.5px; font-weight: 700; color: var(--ink); letter-spacing: -0.3px;
  }
  .overview {
    position: absolute; left: 18px; top: 363px;
    font-size: 17px; font-weight: 300; color: var(--paper); line-height: 24px;
    white-space: nowrap;
  }
  .photo {
    position: absolute; width: 155px; height: 154px;
    border: 2px solid var(--paper);
  }
  .photo--1 { left: 260px; top: 58px; background: linear-gradient(160deg, var(--photo-a), var(--photo-b)); }
  .photo--2 { left: 460px; top: 58px; background: linear-gradient(170deg, var(--photo-c), var(--photo-b)); }
  .photo--3 { left: 262px; top: 271px; background: linear-gradient(160deg, #6e7d7a, var(--photo-a)); }
  .photo--4 { left: 460px; top: 271px; background: linear-gradient(170deg, #5a5f66, var(--photo-d)); }
</style>
</head>
<body>

<section class="slide slide--window">
  <svg class="slide-shapes" width="670" height="472" viewBox="0 0 670 472" aria-hidden="true">
    <polygon points="0,0 150,0 227,98 34,272 0,238" fill="var(--paper)"/>
    <polygon points="161,3 190,20 168,26" fill="var(--gold)"/>
    <polyline points="205,110 227,160 11,260" fill="none" stroke="var(--gold)" stroke-width="3" stroke-dasharray="12 7"/>
  </svg>
  <h2 class="slide-title">Window Display</h2>
  <div class="photo photo--1" role="img" aria-label="Bookstore window display with a tall promotional standee and stacked books"></div>
  <div class="photo photo--2" role="img" aria-label="Wooden bookstore shelf stocked with featured book covers"></div>
  <div class="photo photo--3" role="img" aria-label="Shop window with a promotional standee beside book stacks"></div>
  <div class="photo photo--4" role="img" aria-label="Slatwall display with hanging book cards and red promotional balloons"></div>
  <p class="overview">Overview:<br>3 months in 26 bookstores</p>
</section>

<section class="slide slide--cover">
  <svg class="slide-shapes" width="584" height="397" viewBox="0 0 584 397" aria-hidden="true">
    <polygon points="0,0 114,0 287,175 71,394 0,394" fill="var(--paper)"/>
    <polygon points="184,73 237,97 227,118" fill="var(--gold)"/>
    <polyline points="152,-5 284,283 94,373" fill="none" stroke="var(--gold)" stroke-width="3" stroke-dasharray="12 7"/>
  </svg>
  <div class="brand">
    <span class="brand-square"></span>
    <span class="brand-name">Page Lantern</span>
  </div>
  <ul class="reach-list">
    <li>Comprehensive Window Display, Front Table Placement, and Business Center Pockets.</li>
    <li>45 Airports</li>
    <li>2 Train Stations</li>
    <li>80 Bookstores</li>
  </ul>
</section>

</body>
</html>
```